Business Card for a Floral & Decorating Business

I would like to take my current logo and create a better business card. I am looking for elegance as I am a florist and event decorator. My logo has multiple colour options. I like colours like green, purple, pink and orange, I think I would like a white card, open to black back ground. I want it to feel elegant and romantic. I like metallic lettering that maybe is indented in the paper, I also like glossy paper. I have a full logo already as well as a badge. I have attached both in multiple colours.m
Updates

Need extra days to review

Target Market(s)

Weddings, special events, floral customers

Industry/Entity Type

Floral and decorating

Contact Information for Business Card

Phone number, email, instagram, facebook, title, name, logo

Font styles to use
Script

Requirements
Nice to have
• Elegant

```html
<!DOCTYPE html>
<html lang="en">
<head>
<meta charset="utf-8">
<title>Linden Marlow – Business Card</title>
<link rel="stylesheet" href="https://fonts.googleapis.com/css2?family=Libre+Baskerville:wght@400;700&family=Montserrat:wght@400;500&display=swap">
<style>
  :root {
    --blush: #e8b9aa;
    --blush-soft: #f3d9d0;
    --ink: #2b2b2b;
    --paper: #ffffff;
    --stage: #9b9b9b;
  }
  * { margin: 0; padding: 0; box-sizing: border-box; }
  html, body { width: 1200px; height: 1059px; overflow: hidden; }
  body { background: var(--stage); position: relative; font-family: "Montserrat", sans-serif; }

  .card {
    position: absolute;
    width: 690px;
    height: 392px;
    border-radius: 24px;
    overflow: hidden;
  }
  .card--front { left: 256px; top: 89px; background: var(--paper); }
  .card--back { left: 254px; top: 570px; background: var(--blush); }

  /* Front */
  .brand { position: absolute; left: 32px; top: 58px; width: 300px; color: var(--blush); }
  .brand__name {
    font-family: "Libre Baskerville", serif;
    font-weight: 400;
    font-size: 34px;
    line-height: 1;
    letter-spacing: 0.5px;
  }
  .brand__tagline {
    font-family: "Libre Baskerville", serif;
    font-size: 8.5px;
    letter-spacing: 4px;
    margin: 12px 0 0 72px;
  }
  .accent-bar { position: absolute; left: 0; top: 157px; width: 19px; height: 40px; background: var(--blush); }
  .person { position: absolute; left: 32px; top: 152px; }
  .person__name {
    font-family: "Libre Baskerville", serif;
    font-weight: 700;
    font-size: 25px;
    color: var(--blush);
    line-height: 1.2;
  }
  .person__title { font-size: 16.5px; color: var(--ink); margin-top: 2px; }
  .address { position: absolute; left: 32px; top: 222px; font-size: 16.5px; line-height: 21px; color: var(--ink); }
  .contacts { position: absolute; left: 32px; top: 280px; list-style: none; font-size: 16.5px; color: var(--ink); }
  .contacts li { display: flex; align-items: center; height: 27px; }
  .contacts svg { width: 12px; height: 12px; margin-right: 6px; flex: none; }

  .monogram-art {
    position: absolute;
    left: 417px; top: 26px;
    width: 242px; height: 342px;
    border-radius: 6px;
    background: linear-gradient(160deg, var(--blush-soft), var(--blush));
  }

  /* Back */
  .monogram-art--small {
    left: 309px; top: 54px;
    width: 82px; height: 114px;
    background: linear-gradient(160deg, #f6e3dc, #ffffff);
    opacity: 0.85;
  }
  .brand--back { left: 0; top: 190px; width: 100%; text-align: center; color: var(--paper); }
  .brand--back .brand__name { font-size: 52px; }
  .brand--back .brand__tagline { font-size: 12px; letter-spacing: 7px; margin: 22px 0 0 108px; }
  .social { position: absolute; left: 293px; top: 326px; display: flex; gap: 11px; }
  .social span { width: 29px; height: 29px; border-radius: 7px; background: var(--paper); }
</style>
</head>
<body>

<section class="card card--front">
  <div class="brand">
    <p class="brand__name">Linden Marlow</p>
    <p class="brand__tagline">DECORATING &amp; FLORALS.</p>
  </div>

  <div class="accent-bar"></div>
  <div class="person">
    <h1 class="person__name">ELISE WARREN</h1>
    <p class="person__title">CEO/Founder</p>
  </div>

  <p class="address">42 Willow Lane, Suite B<br>Fairview CA, 93104</p>

  <ul class="contacts">
    <li>
      <svg viewBox="0 0 12 12"><path d="M2.5 1 L4.5 1 L5.3 3.6 L4 4.6 C4.7 6 5.9 7.3 7.4 8 L8.4 6.7 L11 7.5 L11 9.5 C11 10.3 10.3 11 9.5 11 C5 11 1 7 1 2.5 C1 1.7 1.7 1 2.5 1 Z" fill="var(--blush)"/></svg>
      (555) 014-2290
    </li>
    <li>
      <svg viewBox="0 0 12 12"><rect x="0.5" y="2" width="11" height="8" fill="var(--blush)"/><path d="M0.5 2 L6 6.5 L11.5 2" fill="none" stroke="#fff" stroke-width="1"/></svg>
      hello@lindenmarlow.com
    </li>
    <li>
      <svg viewBox="0 0 12 12" fill="none" stroke="var(--blush)" stroke-width="1"><circle cx="6" cy="6" r="5"/><ellipse cx="6" cy="6" rx="2.2" ry="5"/><path d="M1 6 H11 M2 3.5 H10 M2 8.5 H10"/></svg>
      www.lindenmarlow.com
    </li>
  </ul>

  <div class="monogram-art" role="img" aria-label="Large floral line illustration wrapped around a monogram letter"></div>
</section>

<section class="card card--back">
  <div class="monogram-art monogram-art--small" role="img" aria-label="Small floral monogram illustration"></div>
  <div class="brand brand--back">
    <p class="brand__name">Linden Marlow</p>
    <p class="brand__tagline">DECORATING &amp; FLORALS.</p>
  </div>
  <div class="social" aria-label="Social media profiles">
    <span></span><span></span><span></span>
  </div>
</section>

</body>
</html>
```